Strong, modern, clean Business Card design

Looking for a stunning, but CLEAN business card design. While we are a faith-based organization, we do NOT want this to look religious.

Industry/Entity Type

Non-Profit

Contact Information for Business Card

Dale Munroe | Lead Pastor
dale@BrightHarvestHope.org
970-555-0148
PO Box 7316
Loveland, CO 80571

Font styles to use
Serif
Sans Serif

Requirements
Should not have
• Religious imagery or symbolism

```html
<!DOCTYPE html>
<html lang="en">
<head>
<meta charset="utf-8">
<title>Bright Harvest Hope Business Cards</title>
<link rel="stylesheet" href="https://fonts.googleapis.com/css2?family=Playfair+Display:wght@400&family=Roboto:wght@400;700&display=swap">
<style>
  :root {
    --bg: #e9e7e3;
    --card-white: #ffffff;
    --card-dark: #1c1f21;
    --steel-blue: #557f9e;
    --ink: #1f1f1f;
    --muted: #555b60;
    --paper-white: #ffffff;
  }
  * { margin: 0; padding: 0; box-sizing: border-box; }
  html, body {
    width: 1200px; height: 911px; overflow: hidden;
    background: var(--bg);
  }
  .canvas { position: relative; width: 1200px; height: 911px; }
  .card {
    position: absolute; top: 158px;
    width: 340px; height: 595px;
    box-shadow: 0 10px 28px rgba(0,0,0,0.18);
    overflow: hidden;
  }
  .card--front { left: 170px; background: var(--card-white); }
  .card--back { left: 690px; background: var(--card-dark); }

  .org-name {
    position: absolute; left: 30px; right: 30px;
    font-family: "Playfair Display", Georgia, serif;
    font-weight: 400; font-size: 22px; line-height: 1.2;
    text-align: center;
  }
  .card--front .org-name { top: 78px; color: var(--steel-blue); }
  .card--back .org-name { top: 82px; color: var(--paper-white); }

  .contact {
    position: absolute; right: 44px; bottom: 58px;
    text-align: right;
    font-family: "Roboto", Arial, sans-serif;
  }
  .contact__name {
    font-size: 17px; font-weight: 700; color: var(--steel-blue);
    text-transform: uppercase; letter-spacing: 0.5px;
  }
  .contact__title {
    font-size: 13px; font-weight: 700; color: var(--ink);
    text-transform: uppercase; letter-spacing: 0.5px; margin-bottom: 12px;
  }
  .contact__line {
    font-size: 13px; color: var(--muted); line-height: 19px;
    display: flex; justify-content: flex-end; align-items: center; gap: 8px;
  }
  .contact__icon { width: 11px; height: 11px; flex: none; }
  .contact__icon--phone { fill: var(--steel-blue); }
  .contact__icon--mail { fill: none; stroke: var(--steel-blue); stroke-width: 2.4; }
  .contact__spacer { width: 11px; flex: none; }

  .accent-bar {
    position: absolute; right: 0; bottom: 40px;
    width: 22px; height: 120px; background: var(--steel-blue);
  }

  .website {
    position: absolute; top: 128px; left: 0; right: 0;
    text-align: center;
    font-family: "Roboto", Arial, sans-serif;
    font-size: 13px; letter-spacing: 1px; color: var(--paper-white);
  }
  .name-panel {
    position: absolute; left: 26px; right: 26px; bottom: 26px;
    height: 288px; border-radius: 34px;
    background: var(--paper-white);
    display: flex; align-items: center; justify-content: center;
    padding: 0 24px;
  }
  .name-panel__text {
    font-family: "Playfair Display", Georgia, serif;
    font-weight: 400; font-size: 38px; line-height: 1.2;
    text-align: center; color: var(--card-dark);
  }
</style>
</head>
<body>
<main class="canvas">
  <section class="card card--front" aria-label="Business card front">
    <div class="org-name">Bright Harvest Hope</div>
    <div class="contact">
      <div class="contact__name">Dale Munroe</div>
      <div class="contact__title">Lead Pastor</div>
      <div class="contact__line">PO Box 7316<span class="contact__spacer"></span></div>
      <div class="contact__line">Loveland, CO 80571<span class="contact__spacer"></span></div>
      <div class="contact__line">970-555-0148
        <svg class="contact__icon contact__icon--phone" viewBox="0 0 24 24" aria-hidden="true"><path d="M6.6 10.8a15.1 15.1 0 0 0 6.6 6.6l2.2-2.2a1 1 0 0 1 1-.25 11.4 11.4 0 0 0 3.6.57 1 1 0 0 1 1 1V20a1 1 0 0 1-1 1A17 17 0 0 1 3 4a1 1 0 0 1 1-1h3.5a1 1 0 0 1 1 1c0 1.25.2 2.45.57 3.57a1 1 0 0 1-.25 1z"/></svg>
      </div>
      <div class="contact__line">dale@BrightHarvestHope.org
        <svg class="contact__icon contact__icon--mail" viewBox="0 0 24 24" aria-hidden="true"><rect x="2" y="5" width="20" height="14"/><path d="M2 5l10 8 10-8"/></svg>
      </div>
    </div>
    <div class="accent-bar"></div>
  </section>

  <section class="card card--back" aria-label="Business card back">
    <div class="org-name">Bright Harvest Hope</div>
    <div class="website">brightharvesthope.org</div>
    <div class="name-panel">
      <span class="name-panel__text">Bright Harvest Hope</span>
    </div>
  </section>
</main>
</body>
</html>
```